Motivational Poster Series for Students at Truck Driving School

We are looking for a series of 3 motivational posters (18"X 24") to be used in classrooms at a truck driving school. The audience for the posters will be the students that are currently in school and the purpose of the posters is to be motivational pieces that will be displayed on the walls.

We have provided the quotes below that are to be used on each poster. We have also provided some example images from PixVaultImages to give an idea on the backgrounds that we'd like to see on each poster. The images do not have to be exact, these are just examples of what we think will look good for each quote. Since this is a series, they can all be somewhat similar in look/feel - just with different images and quotes.

So, the basic idea is a background image/design with a quote being the main point of emphasis. Other than that, we would like to include the logo provided at a small scale in one of the corners of the poster as a watermark for branding purposes.

Below are the quotes for each of the 3 posters:

Poster 1 - “It’s very difficult to follow our dreams, but it’s even more difficult to forget them.” - Devan Okafor

Poster 2 - “Success doesn’t just come and find you, you have to go out and get it.” - Unknown

Poster 3 - “If you are not willing to learn, no one can help you. If you are determined to learn, no one can stop you.”
- Unknown

NOTE: these posters should be designed as 18" X 24" in size with 2 of them being landscape and one being portrait orientation (as shown in images provided below)

Below are some sample images to give an idea on what could be used as background design for each quote. The logo that should be used as a watermark in a corner for some subtle branding has been provided as well.

Target Market(s)

The target market for this series are truck drivers between the ages of 25-55. Mostly males.

Industry/Entity Type

Landscape

Requirements
Must have
• Quote featured, high quality background design/image, logo watermark

```html
<!DOCTYPE html>
<html lang="en">
<head>
<meta charset="utf-8">
<title>Follow Your Dreams – Motivational Poster</title>
<link rel="stylesheet" href="https://fonts.googleapis.com/css2?family=Quicksand:wght@500;600&display=swap">
<style>
  :root {
    --paper: #ffffff;
    --frame-green: #1f7a4c;
    --sign-green: #1d7a4e;
    --sign-edge: #e9f1ec;
    --sign-text: #ffffff;
    --pole-light: #d9dcde;
    --pole-dark: #7d8285;
    --sky-light: #eef3f4;
    --sky-mid: #b9cdd4;
    --shade: #1b2421;
    --field: #3f5a2a;
  }
  html, body {
    margin: 0;
    padding: 0;
    width: 1200px;
    height: 900px;
    overflow: hidden;
    background: var(--paper);
  }
  .poster {
    position: relative;
    width: 1200px;
    height: 900px;
    background: var(--paper);
    font-family: "Quicksand", sans-serif;
  }
  .poster__frame {
    position: absolute;
    left: 18px;
    top: 20px;
    width: 1158px;
    height: 853px;
    border: 3px solid var(--frame-green);
    overflow: hidden;
  }
  .poster__scene {
    position: absolute;
    inset: 0;
    background:
      radial-gradient(ellipse 70% 75% at 42% 40%, rgba(255,255,255,0.85) 0%, rgba(255,255,255,0) 70%),
      linear-gradient(90deg, rgba(0,0,0,0) 55%, rgba(20,28,26,0.85) 100%),
      linear-gradient(180deg, var(--sky-mid) 0%, var(--sky-light) 40%, #c9d6d6 58%, #2a3b22 62%, #56713a 72%, #d6dcd8 76%, #d9ded9 79%, var(--field) 81%, #2f4a22 100%);
  }
  .sign {
    position: absolute;
    left: 178px;
    top: 84px;
    width: 304px;
    height: 795px;
  }
  .sign__art {
    position: absolute;
    inset: 0;
  }
  .sign__quote {
    position: absolute;
    left: 52px;
    top: 95px;
    width: 200px;
    margin: 0;
    text-align: center;
    color: var(--sign-text);
    font-size: 17px;
    font-weight: 500;
    line-height: 1.2;
  }
  .sign__author {
    display: block;
    margin-top: 16px;
    font-size: 12.5px;
    font-style: italic;
  }
  .sign__brand {
    position: absolute;
    left: 70px;
    top: 340px;
    width: 166px;
    height: 62px;
    display: flex;
    align-items: center;
    justify-content: center;
    gap: 7px;
    color: var(--sign-text);
    font-size: 13px;
    font-weight: 600;
    line-height: 1.1;
  }
  .sign__brand-dot {
    width: 16px;
    height: 16px;
    border-radius: 50%;
    background: var(--sign-text);
    flex: none;
  }
</style>
</head>
<body>
  <main class="poster">
    <div class="poster__frame">
      <div class="poster__scene" role="img" aria-label="Semi truck with white trailer and blue cab driving along a highway past green fields and trees under a cloudy sky"></div>
    </div>

    <div class="sign">
      <svg class="sign__art" width="304" height="795" viewBox="0 0 304 795" aria-hidden="true">
        <defs>
          <linearGradient id="pole-shine" x1="0" x2="1">
            <stop offset="0" stop-color="var(--pole-dark)"/>
            <stop offset="0.45" stop-color="var(--pole-light)"/>
            <stop offset="1" stop-color="var(--pole-dark)"/>
          </linearGradient>
        </defs>
        <rect x="143" y="0" width="18" height="795" fill="url(#pole-shine)"/>
        <rect x="152" y="8" width="212" height="212" rx="14" transform="rotate(45 152 8)" fill="var(--sign-green)"/>
        <rect x="152" y="20" width="195" height="195" rx="11" transform="rotate(45 152 20)" fill="none" stroke="var(--sign-edge)" stroke-width="3"/>
        <circle cx="152" cy="26" r="3" fill="var(--sign-edge)"/>
        <circle cx="152" cy="286" r="3" fill="var(--sign-edge)"/>
        <rect x="65" y="326" width="176" height="72" rx="7" fill="var(--sign-green)"/>
        <rect x="71" y="332" width="164" height="60" rx="5" fill="none" stroke="var(--sign-edge)" stroke-width="3"/>
      </svg>

      <p class="sign__quote">“It’s very difficult to follow our dreams but it’s even more difficult to forget them.”
        <span class="sign__author">- Devan Okafor</span>
      </p>

      <div class="sign__brand">
        <span class="sign__brand-dot"></span>
        <span>Milepost Driver<br>Academy</span>
      </div>
    </div>
  </main>
</body>
</html>
```